We are in search of a new business card design for our business. We have a Mexican Grocery Store called Tortilla Grove Market, we would like to see that some have mexican design, but we are open to any type of designs.

Phone: to be announced
Fax: to be announced

Address is:
2415 Calloway Blvd
Harlow Point, MD 21490

```html
<!DOCTYPE html>
<html lang="en">
<head>
<meta charset="utf-8">
<title>Tortilla Grove Market – Business Card</title>
<link rel="stylesheet" href="https://fonts.googleapis.com/css2?family=Open+Sans:wght@400;700;800&display=swap">
<style>
  :root {
    --page-bg: #ebe8e6;
    --card-white: #ffffff;
    --accent-green: #1f7a12;
    --band-red-light: #b50d18;
    --band-red: #990812;
    --band-red-dark: #6e040b;
    --brand-red: #a10711;
    --text-light: #ffffff;
  }
  * { box-sizing: border-box; margin: 0; padding: 0; }
  html, body {
    width: 1019px;
    height: 1200px;
    overflow: hidden;
    background: var(--page-bg);
    font-family: "Open Sans", Arial, sans-serif;
  }
  .business-card {
    position: absolute;
    left: 60px;
    top: 343px;
    width: 900px;
    height: 514px;
    background: var(--card-white);
    box-shadow: 0 6px 24px rgba(0,0,0,0.18);
    overflow: hidden;
  }
  .top-rule {
    position: absolute;
    left: 0; top: 0;
    width: 100%;
    height: 10px;
    background: var(--accent-green);
  }
  .contact-band {
    position: absolute;
    left: 0; bottom: 0;
    width: 100%;
    height: 264px;
    background:
      radial-gradient(ellipse 60% 90% at 50% 25%, var(--band-red-light) 0%, transparent 70%),
      linear-gradient(180deg, var(--band-red) 0%, var(--band-red-dark) 100%);
  }
  .brand-mark {
    position: absolute;
    left: 0; top: 120px;
    width: 100%;
    display: flex;
    align-items: center;
    justify-content: center;
    gap: 18px;
  }
  .brand-dot {
    width: 26px;
    height: 26px;
    border-radius: 50%;
    background: var(--accent-green);
  }
  .brand-name {
    font-weight: 800;
    font-size: 54px;
    color: var(--brand-red);
    letter-spacing: -0.5px;
  }
  .contact-info {
    position: absolute;
    bottom: 38px;
    color: var(--text-light);
    font-size: 23px;
    line-height: 32px;
  }
  .contact-info strong { font-weight: 700; }
  .contact-phone { left: 37px; }
  .contact-address { right: 37px; text-align: right; }
</style>
</head>
<body>
  <div class="business-card">
    <div class="top-rule"></div>
    <div class="contact-band"></div>
    <div class="brand-mark">
      <span class="brand-dot"></span>
      <span class="brand-name">Tortilla Grove Market</span>
    </div>
    <div class="contact-info contact-phone">
      <p><strong>Phone:</strong> to be announced</p>
      <p><strong>Fax:</strong> to be announced</p>
    </div>
    <div class="contact-info contact-address">
      <p><strong>Address</strong></p>
      <p>2415 Calloway Blvd</p>
      <p>Harlow Point, MD 21490</p>
    </div>
  </div>
</body>
</html>
```